Medical IT Business with New logo needs a fresh stationary design

First time on sketch Harbor; Thought I would give it a go.
This project is for business cards alone but we have loads of design work that needs to take place in the immediate future.

We provide IT services to the Medical Industry and value ourselves as offering a premium product to the market.

I am after a fresh, clean design using full colour 2 sided cards which includes our current colour palettes from our logo.

Card's must include:
- Logo
- Slogan
- Name
- Adress
- Email
- Phone
- Fax
- Mobile

Target Market(s)

Surgeons, High Profile Medical Personnel

Industry/Entity Type

Business

Fonts, CMYK Colours and Logo files attached.

Requirements
Must have
• Card's must include:
• - Logo
• - Slogan
• - Name
• - Adress
• - Email
• - Phone
• - Fax
• - Mobile
Nice to have
• Needs to incorporate our colour palette (attached CMYK colours)
Should not have
• Black backgrounds. Black text ok.

```html
<!DOCTYPE html>
<html lang="en">
<head>
<meta charset="utf-8">
<title>Clinova Systems – Business Cards</title>
<link rel="stylesheet" href="https://fonts.googleapis.com/css2?family=Oswald:wght@300;500&family=Open+Sans:wght@600&display=swap">
<style>
  :root {
    --canvas: #e6e6e6;
    --card-top: #e9e9e9;
    --card-mid: #f2f2f2;
    --card-mid-edge: #e6e6e6;
    --card-bottom: #f8f8f8;
    --navy: #0f3a68;
    --brand-blue: #1380b5;
    --chevron-blue: #0380b8;
    --panel-blue: #008fd5;
    --steel: #85888b;
    --slogan: #7d8084;
    --white: #ffffff;
  }
  * { margin: 0; padding: 0; box-sizing: border-box; }
  html, body { width: 1200px; height: 1200px; overflow: hidden; }
  body { background: var(--canvas); position: relative; font-family: "Open Sans", sans-serif; }

  .card {
    position: absolute;
    left: 210px;
    width: 780px;
    height: 444px;
    overflow: hidden;
    box-shadow: 0 6px 18px rgba(0,0,0,0.08);
  }
  .card--front { top: 140px; }
  .card--back { top: 650px; }
  .card__art { position: absolute; inset: 0; width: 780px; height: 444px; }

  .brand { position: absolute; display: flex; align-items: center; }
  .brand__dot {
    flex: none;
    border-radius: 50%;
    background: var(--brand-blue);
  }
  .brand__name {
    font-family: "Oswald", sans-serif;
    font-weight: 500;
    color: var(--navy);
    text-transform: uppercase;
    line-height: 0.95;
    letter-spacing: 0.5px;
  }
  .brand__name span { display: block; }

  .card--front .brand { left: 30px; top: 160px; }
  .card--front .brand__dot { width: 110px; height: 110px; margin-right: 22px; }
  .card--front .brand__name { font-size: 64px; }

  .card--back .brand { left: 24px; top: 140px; }
  .card--back .brand__dot { width: 100px; height: 100px; margin-right: 20px; }
  .card--back .brand__name { font-size: 56px; }

  .slogan {
    position: absolute;
    left: 144px;
    top: 262px;
    font-family: "Oswald", sans-serif;
    font-weight: 300;
    font-size: 23px;
    color: var(--slogan);
  }

  .contact {
    position: absolute;
    left: 510px;
    top: 146px;
    list-style: none;
    color: var(--white);
    font-size: 11px;
    line-height: 15.5px;
    letter-spacing: 0.2px;
  }
  .contact__item { display: flex; align-items: center; }
  .contact__item + .contact__item { margin-top: 15px; }
  .contact__icon { width: 22px; height: 22px; flex: none; margin-right: 14px; fill: var(--white); }
</style>
</head>
<body>

  <!-- Front of card -->
  <section class="card card--front" aria-label="Business card front">
    <svg class="card__art" viewBox="0 0 780 444" aria-hidden="true">
      <defs>
        <linearGradient id="midBandFront" x1="0" y1="0" x2="0" y2="1">
          <stop offset="0" stop-color="var(--card-mid)"/>
          <stop offset="1" stop-color="var(--card-mid-edge)"/>
        </linearGradient>
      </defs>
      <rect width="780" height="444" fill="var(--card-bottom)"/>
      <rect width="780" height="84" fill="var(--card-top)"/>
      <polygon points="0,84 550,84 530,100 530,342 550,358 0,358" fill="url(#midBandFront)"/>
      <polygon points="339,108 389,108 472,222 389,335 339,335 422,222" fill="var(--chevron-blue)"/>
      <polygon points="405,108 780,108 780,335 405,335 488,222" fill="var(--steel)"/>
    </svg>
    <div class="brand">
      <div class="brand__dot"></div>
      <h1 class="brand__name"><span>Clinova</span><span>Systems</span></h1>
    </div>
  </section>

  <!-- Back of card -->
  <section class="card card--back" aria-label="Business card back">
    <svg class="card__art" viewBox="0 0 780 444" aria-hidden="true">
      <defs>
        <linearGradient id="midBandBack" x1="0" y1="0" x2="0" y2="1">
          <stop offset="0" stop-color="var(--card-mid)"/>
          <stop offset="1" stop-color="var(--card-mid-edge)"/>
        </linearGradient>
      </defs>
      <rect width="780" height="444" fill="var(--card-bottom)"/>
      <rect width="780" height="84" fill="var(--card-top)"/>
      <polygon points="0,84 550,84 530,100 530,342 550,358 0,358" fill="url(#midBandBack)"/>
      <polygon points="339,108 389,108 472,222 389,335 339,335 422,222" fill="var(--steel)"/>
      <polygon points="405,108 780,108 780,335 405,335 488,222" fill="var(--panel-blue)"/>
    </svg>
    <div class="brand">
      <div class="brand__dot"></div>
      <h2 class="brand__name"><span>Clinova</span><span>Systems</span></h2>
    </div>
    <p class="slogan">online with your practice</p>

    <ul class="contact">
      <li class="contact__item">
        <svg class="contact__icon" viewBox="0 0 24 24" aria-hidden="true"><path d="M2 5h20v14H2z M3.5 6.5v.3l8.5 6.2 8.5-6.2v-.3z M3.5 8.6v8.9l5.6-4.8z M20.5 8.6l-5.6 4.1 5.6 4.8z M10.3 13.6l-6.2 5.4h15.8l-6.2-5.4L12 14.9z" fill-rule="evenodd"/></svg>
        <span>INFO@COMPANYNAME.COM</span>
      </li>
      <li class="contact__item">
        <svg class="contact__icon" viewBox="0 0 24 24" aria-hidden="true"><path d="M6.6 2.5l3 3.2-1.8 2.6c1.2 2.8 3.4 5 6.2 6.3l2.6-1.8 3.2 3-2.3 3.4C10 19 5 14 4 4.8z"/></svg>
        <span>+18 5510 3362 0914<br>+18 5510 3362 0927</span>
      </li>
      <li class="contact__item">
        <svg class="contact__icon" viewBox="0 0 24 24" aria-hidden="true"><path d="M12 3L1.5 12h3v9h6v-6h3v6h6v-9h3z"/></svg>
        <span>YOUR CITY ADDRESS<br>STREET LOCATION, NY CITY, USA</span>
      </li>
      <li class="contact__item">
        <svg class="contact__icon" viewBox="0 0 24 24" aria-hidden="true"><path d="M12 2a10 10 0 1 0 0 20 10 10 0 0 0 0-20zm-1 3.2c-.6 1.3-2.4 1.6-2.6 3-.2 1.2 1.6 1.4 2 2.6.4 1.2-1.4 2-.8 3.4.5 1.2 2 1 2.2 2.6.1.9-.3 2-.6 2.8A7.9 7.9 0 0 1 5 9.2c1.6-.2 2.4-2.4 4.2-3.2.6-.3 1.2-.6 1.8-.8zm3.6.4a8 8 0 0 1 5.2 8.2c-.9-.5-1.6-1.6-2.7-1.4-1.2.3-1.8-1-2.6-1.6-.8-.6-.1-1.8.5-2.4.6-.6-.8-1.6-.4-2.8z" fill-rule="evenodd"/></svg>
        <span>WWW.COMPANY-NAME.COM</span>
      </li>
    </ul>
  </section>

</body>
</html>
```